Brightmark Electrical Flyer

An eye catching flyer design which showcases the type of work we do in the electrical industry in Vancouver,BC. The final design should be simple and incorporate our logo. And present a high end company.

Industry/Entity Type

Electrical

```html
<!DOCTYPE html>
<html lang="en">
<head>
<meta charset="utf-8">
<title>Brightmark Electrical Flyer</title>
<link rel="stylesheet" href="https://fonts.googleapis.com/css2?family=Oswald:wght@400;600;700&family=Roboto+Condensed:wght@400;700&family=Roboto:wght@400;500;700&display=swap">
<style>
  :root {
    --yellow: #f5c800;
    --yellow-deep: #e8b400;
    --yellow-soft: #fbe27a;
    --cream: #fbf7e4;
    --charcoal: #3b3b3b;
    --graphite: #555555;
    --text: #2e2e2e;
    --white: #ffffff;
  }
  * { margin: 0; padding: 0; box-sizing: border-box; }
  html, body { width: 970px; height: 1200px; overflow: hidden; background: #e9e9e9; }
  .flyer {
    position: relative; width: 970px; height: 1200px; overflow: hidden;
    background: var(--cream);
    font-family: "Roboto", Arial, sans-serif; color: var(--text);
  }
  .flyer-shapes { position: absolute; inset: 0; }

  .brand { position: absolute; left: 40px; top: 40px; }
  .brand-row { display: flex; align-items: center; gap: 12px; }
  .brand-dot { width: 26px; height: 26px; border-radius: 50%; background: var(--yellow); }
  .brand-name {
    font-family: "Roboto Condensed", Arial, sans-serif; font-weight: 700;
    font-size: 34px; color: var(--charcoal); letter-spacing: 0.5px;
  }
  .brand-url {
    margin-top: 8px; font-family: "Roboto", Arial, sans-serif; font-weight: 700;
    font-size: 20px; color: var(--charcoal);
  }

  .headline { position: absolute; right: 32px; top: 50px; text-align: right; }
  .headline-title {
    font-family: "Oswald", Arial, sans-serif; font-weight: 700; font-size: 64px;
    line-height: 1; letter-spacing: 1px; color: #2f2f2f;
  }
  .headline-tagline {
    margin-top: 8px; font-family: "Roboto Condensed", Arial, sans-serif; font-weight: 700;
    font-size: 17px; color: #2f2f2f; letter-spacing: 0.4px;
  }

  .about {
    position: absolute; left: 45px; top: 515px; width: 342px; height: 150px;
    background: linear-gradient(#5a5a5a, #3a3a3a); border-radius: 0 0 18px 18px;
    padding: 18px 20px; color: var(--white);
    box-shadow: 0 6px 10px rgba(0,0,0,0.25);
  }
  .about-title { font-family: "Roboto Condensed", Arial, sans-serif; font-weight: 700; font-size: 24px; color: var(--yellow); }
  .about-text { margin-top: 6px; font-family: "Roboto Condensed", Arial, sans-serif; font-size: 19px; line-height: 1.3; }

  .services { position: absolute; left: 42px; top: 698px; width: 480px; }
  .services-title { font-family: "Oswald", Arial, sans-serif; font-weight: 400; font-size: 54px; line-height: 1; color: #454545; letter-spacing: -0.5px; }
  .services-intro { margin-top: 14px; font-size: 13.5px; font-weight: 700; line-height: 1.35; color: #444; }
  .services-sectors { margin-top: 14px; display: flex; gap: 18px; font-weight: 500; font-size: 19px; color: #333; }
  .services-sectors span::before { content: "\2022"; color: var(--yellow-deep); margin-right: 7px; }
  .service-list { list-style: none; margin-top: 20px; }
  .service-item { position: relative; padding-left: 26px; margin-bottom: 14px; }
  .service-tick { position: absolute; left: 0; top: 0; width: 20px; height: 18px; }
  .service-name { font-family: "Roboto Condensed", Arial, sans-serif; font-weight: 700; font-size: 15px; color: #222; }
  .service-desc { font-size: 13.5px; color: #333; line-height: 1.3; }

  .contact {
    position: absolute; left: 80px; top: 1148px; font-size: 16px; line-height: 1.6;
    color: var(--yellow);
  }
  .contact-line { display: flex; align-items: center; gap: 8px; }
  .contact-icon { width: 12px; height: 12px; }

  .feature { position: absolute; color: #222; }
  .feature-title { font-family: "Roboto Condensed", Arial, sans-serif; font-weight: 700; font-size: 17px; }
  .feature-text { font-family: "Roboto Condensed", Arial, sans-serif; font-size: 14.5px; line-height: 1.3; }
  .feature--lighting { left: 700px; top: 640px; width: 190px; }
  .feature--smart { left: 726px; top: 832px; width: 220px; }
  .feature--construction { left: 760px; top: 1008px; width: 200px; }
  .feature--construction .feature-title { font-size: 15px; }
  .feature--construction .feature-text { font-size: 13.5px; }

  .phone { position: absolute; left: 712px; top: 1100px; width: 240px; text-align: center; color: var(--white); }
  .phone-icon { width: 30px; height: 30px; display: block; margin: 0 auto 4px; }
  .phone-number { font-family: "Oswald", Arial, sans-serif; font-weight: 400; font-size: 42px; line-height: 1; }
</style>
</head>
<body>
<main class="flyer">
  <svg class="flyer-shapes" width="970" height="1200" viewBox="0 0 970 1200" aria-hidden="false">
    <defs>
      <linearGradient id="lobbyTone" x1="0" y1="0" x2="0" y2="1">
        <stop offset="0" stop-color="#f1f3f8"/>
        <stop offset="0.35" stop-color="#c9cfe4"/>
        <stop offset="0.7" stop-color="#9aa3c6"/>
        <stop offset="1" stop-color="#7e7f96"/>
      </linearGradient>
      <linearGradient id="headerTone" x1="0" y1="0" x2="0" y2="1">
        <stop offset="0" stop-color="#ffffff"/>
        <stop offset="1" stop-color="#dcdcdc"/>
      </linearGradient>
      <linearGradient id="panelTone" x1="0" y1="0" x2="1" y2="1">
        <stop offset="0" stop-color="#fbe36a"/>
        <stop offset="0.5" stop-color="#f6cf1c"/>
        <stop offset="1" stop-color="#f2c200"/>
      </linearGradient>
      <radialGradient id="corridorTone" cx="0.5" cy="0.5" r="0.6">
        <stop offset="0" stop-color="#ffd36a"/>
        <stop offset="0.6" stop-color="#d8682a"/>
        <stop offset="1" stop-color="#6b2414"/>
      </radialGradient>
      <linearGradient id="rackTone" x1="0" y1="0" x2="1" y2="0">
        <stop offset="0" stop-color="#1c2433"/>
        <stop offset="0.5" stop-color="#4c5a78"/>
        <stop offset="1" stop-color="#20283a"/>
      </linearGradient>
      <linearGradient id="workerTone" x1="0" y1="0" x2="1" y2="1">
        <stop offset="0" stop-color="#cfd3d8"/>
        <stop offset="0.5" stop-color="#b5894f"/>
        <stop offset="1" stop-color="#f0c400"/>
      </linearGradient>
      <linearGradient id="tabTone" x1="0" y1="0" x2="0" y2="1">
        <stop offset="0" stop-color="#555"/>
        <stop offset="1" stop-color="#333"/>
      </linearGradient>
    </defs>

    <!-- lobby photo area -->
    <path role="img" aria-label="Photo of a bright modern office lobby with blue walls, glossy tiled floor, reception desk and meeting room"
          d="M0,120 H970 V720 C880,640 740,575 540,555 C340,535 170,480 0,478 Z" fill="url(#lobbyTone)"/>

    <!-- header bands -->
    <rect x="0" y="0" width="970" height="130" fill="url(#headerTone)"/>
    <path d="M0,0 H520 C470,110 380,200 0,210 Z" fill="#ffffff"/>
    <path d="M0,210 C380,200 470,110 520,0 L526,0 C480,118 392,208 0,218 Z" fill="#9a9a9a"/>
    <path d="M0,224 C395,214 488,122 540,0 L560,0 C505,140 410,246 0,262 Z" fill="var(--yellow)"/>

    <!-- bottom swoosh of photo -->
    <path d="M0,478 C170,480 340,535 540,555 C740,575 880,640 970,720 V735 C880,665 740,600 540,580 C340,560 170,512 0,515 Z" fill="var(--yellow)"/>
    <path d="M540,580 C740,600 880,665 970,735 V760 C880,690 740,622 540,598 Z" fill="#6b6b6b"/>

    <!-- yellow services panel -->
    <path d="M470,590 C500,588 520,590 540,598 C740,622 880,690 970,760 V1200 H666 C640,1000 570,800 470,590 Z" fill="var(--yellow-soft)"/>
    <path role="img" aria-label="Faint photo of an electrical distribution panel behind the yellow panel"
          d="M510,600 C740,625 880,692 970,762 V1200 H700 C680,1000 610,800 510,600 Z" fill="url(#panelTone)"/>

    <!-- feature circles -->
    <circle cx="555" cy="655" r="88" fill="#ffffff" opacity="0.85"/>
    <circle role="img" aria-label="Photo of a lit corridor with warm red and yellow lighting" cx="555" cy="655" r="80" fill="url(#corridorTone)"/>
    <circle cx="630" cy="855" r="86" fill="#ffffff" opacity="0.85"/>
    <circle role="img" aria-label="Photo of server racks with small blue lights" cx="630" cy="855" r="78" fill="url(#rackTone)"/>
    <circle cx="672" cy="1030" r="80" fill="#ffffff" opacity="0.85"/>
    <circle role="img" aria-label="Photo of an electrician holding a yellow hard hat with a tool belt" cx="672" cy="1030" r="72" fill="url(#workerTone)"/>

    <!-- contact tab -->
    <path d="M0,1136 H440 C480,1136 500,1200 540,1200 H0 Z" fill="url(#tabTone)"/>
  </svg>

  <header class="brand">
    <div class="brand-row">
      <span class="brand-dot"></span>
      <span class="brand-name">Brightmark Electrical</span>
    </div>
    <div class="brand-url">www.brightmarkelectrical.ca</div>
  </header>

  <div class="headline">
    <h1 class="headline-title">BUILDING DREAMS</h1>
    <p class="headline-tagline">EXPERT DESIGNERS TURN YOUR DREAMS INTO REALITY</p>
  </div>

  <section class="about">
    <h2 class="about-title">About Us</h2>
    <p class="about-text">We are an electrical contractor serving the lower mainland. Providing the best in customer service and knowledge, to our clients.</p>
  </section>

  <section class="services">
    <h2 class="services-title">Our Services</h2>
    <p class="services-intro">Brightmark Electrical offers a wide varierty of services, to meet your electrical needs. Whether it may be residential, commercial or industrial.</p>
    <div class="services-sectors"><span>Residential</span><span>Commerical</span><span>Lighting</span></div>
    <ul class="service-list">
      <li class="service-item">
        <svg class="service-tick" viewBox="0 0 20 18"><path d="M2,10 L7,15 L18,2" fill="none" stroke="#e8b400" stroke-width="3.2" stroke-linecap="round" stroke-linejoin="round"/></svg>
        <div class="service-name">Service</div>
        <div class="service-desc">initial electrical service, and electrical upgrades</div>
      </li>
      <li class="service-item">
        <svg class="service-tick" viewBox="0 0 20 18"><path d="M2,10 L7,15 L18,2" fill="none" stroke="#e8b400" stroke-width="3.2" stroke-linecap="round" stroke-linejoin="round"/></svg>
        <div class="service-name">Fire Alarm</div>
        <div class="service-desc">Providing fire alarm systems and life safety</div>
      </li>
      <li class="service-item">
        <svg class="service-tick" viewBox="0 0 20 18"><path d="M2,10 L7,15 L18,2" fill="none" stroke="#e8b400" stroke-width="3.2" stroke-linecap="round" stroke-linejoin="round"/></svg>
        <div class="service-name">Low Voltage Wiring</div>
        <div class="service-desc">Data and telecommunications services, from rough-in to<br>completion</div>
      </li>
      <li class="service-item">
        <svg class="service-tick" viewBox="0 0 20 18"><path d="M2,10 L7,15 L18,2" fill="none" stroke="#e8b400" stroke-width="3.2" stroke-linecap="round" stroke-linejoin="round"/></svg>
        <div class="service-name">Security</div>
        <div class="service-desc">Full security rough-in and complete monitoring solutions</div>
      </li>
      <li class="service-item">
        <svg class="service-tick" viewBox="0 0 20 18"><path d="M2,10 L7,15 L18,2" fill="none" stroke="#e8b400" stroke-width="3.2" stroke-linecap="round" stroke-linejoin="round"/></svg>
        <div class="service-name">Solar Panel</div>
        <div class="service-desc">Solar panel installations and energy efficient homes</div>
      </li>
    </ul>
  </section>

  <div class="feature feature--lighting">
    <h3 class="feature-title">Lighting Experts</h3>
    <p class="feature-text">We provide all your lighting needs to complete any project from small to large.</p>
  </div>
  <div class="feature feature--smart">
    <h3 class="feature-title">Panelized Smart Lighting</h3>
    <p class="feature-text">Smart lighting solutions give you endless options with your lights</p>
  </div>
  <div class="feature feature--construction">
    <h3 class="feature-title">Quality On Time Construction</h3>
    <p class="feature-text">We efficiently manage construction and coordinate with schedules to always give our clients an effortless experience.</p>
  </div>

  <div class="contact">
    <div class="contact-line">
      <svg class="contact-icon" viewBox="0 0 12 12"><rect x="0.8" y="2" width="10.4" height="8" fill="none" stroke="#dddddd" stroke-width="1.2"/><path d="M1,2.5 L6,7 L11,2.5" fill="none" stroke="#dddddd" stroke-width="1.2"/></svg>
      <span>info@brightmarkelectrical.ca</span>
    </div>
    <div class="contact-line">
      <svg class="contact-icon" viewBox="0 0 12 12"><circle cx="6" cy="6" r="5" fill="#dddddd"/></svg>
      <span>www.brightmarkelectrical.ca</span>
    </div>
  </div>

  <div class="phone">
    <svg class="phone-icon" viewBox="0 0 30 30"><circle cx="15" cy="15" r="13" fill="none" stroke="#222" stroke-width="2"/><path d="M10,8 L13,8 L14,12 L12,13.5 C13,16 14,17 16.5,18 L18,16 L22,17 L22,20 C22,21 21,22 20,22 C14,21.5 8.5,16 8,10 C8,9 9,8 10,8 Z" fill="#222"/></svg>
    <div class="phone-number">604 555 0148</div>
  </div>
</main>
</body>
</html>
```